Rewards Postcard

We are a women's apparel store in Illinois and Iowa and we have a rewards program, we send rewards postcards - but the ones we send are not very good and don't really convey a nice sense of a true thank you, it currently looks just like a coupon postcard. I would really like the customer know that it is a reward. I am going to attach several examples of our previous things we have done - I will make a note on what we like or don't like.

Target Market(s)

existing cusotmers

Industry/Entity Type

Womens Clothing

```html
<!DOCTYPE html>
<html lang="en">
<head>
<meta charset="utf-8">
<title>Maple Row Rewards Postcard</title>
<link href="https://fonts.googleapis.com/css2?family=Lato:wght@400;700&family=Lobster&family=Oswald:wght@500;700&display=swap" rel="stylesheet">
<style>
  :root {
    --stage: #7a5233;
    --paper: #ffffff;
    --red: #e3141b;
    --red-deep: #b80d12;
    --charcoal: #2e2e30;
    --ink: #1c1c1c;
    --rule: #9a9a9a;
    --photo-a: #e9dcd2;
    --photo-b: #c9b6a4;
  }
  * { margin: 0; padding: 0; box-sizing: border-box; }
  html, body { width: 907px; height: 1200px; overflow: hidden; }
  body { background: var(--stage); position: relative; font-family: "Lato", sans-serif; }

  .postcard {
    position: absolute; left: 123px; width: 659px;
    background: var(--paper); overflow: hidden;
    box-shadow: 0 4px 10px rgba(0,0,0,.35);
  }
  .postcard--front { top: 54px; height: 512px; }
  .postcard--back { top: 613px; height: 510px; }
  .postcard svg.shapes { position: absolute; inset: 0; }

  .brand {
    position: absolute; left: 22px; top: 74px;
    font-family: "Lato", sans-serif; font-weight: 700; font-size: 22px;
    letter-spacing: 2px; color: var(--ink);
    display: flex; align-items: center; gap: 8px;
  }
  .brand__dot { width: 10px; height: 10px; background: var(--red); border-radius: 50%; }

  .offer { position: absolute; left: 0; width: 296px; text-align: center; color: #fff; }
  .offer__now { top: 224px; font-family: "Lobster", cursive; font-size: 44px; line-height: 1.1; }
  .offer__program { top: 276px; font-family: "Lobster", cursive; font-size: 24px; }
  .offer__more { top: 309px; font-size: 20px; font-weight: 700; }
  .offer__amount {
    position: absolute; left: 80px; top: 342px;
    font-family: "Oswald", sans-serif; font-weight: 700; font-size: 76px; line-height: 1;
    color: var(--charcoal); -webkit-text-stroke: 2px #fff;
  }
  .offer__label {
    position: absolute; left: 211px; top: 370px;
    font-family: "Oswald", sans-serif; font-weight: 500; font-size: 21px; color: #fff;
  }

  .front-contact { position: absolute; right: 52px; top: 414px; list-style: none; text-align: right; color: #fff; }
  .front-contact li { font-size: 15.5px; height: 26.5px; display: flex; justify-content: flex-end; align-items: center; gap: 12px; }
  .front-contact li:first-child { font-weight: 700; }
  .front-contact svg { width: 12px; height: 12px; fill: var(--red); margin-right: -30px; }

  .thanks {
    position: absolute; left: 22px; top: 18px;
    font-family: "Lobster", cursive; font-weight: 400; font-size: 36px; color: #fff;
  }
  .letter { position: absolute; left: 20px; top: 98px; width: 330px; color: var(--ink); }
  .letter__wrap {
    float: right; width: 60px; height: 240px;
    shape-outside: polygon(58px 0, 60px 0, 60px 240px, 28px 240px, 38px 160px, 46px 100px);
  }
  .letter__greeting { font-weight: 700; font-size: 14.5px; margin-bottom: 10px; }
  .letter__body { font-size: 12.6px; line-height: 15.5px; padding-left: 2px; text-align: justify; }
  .letter__sign { font-weight: 700; font-size: 14px; margin-top: 12px; }

  .back-contact { position: absolute; left: 24px; top: 344px; list-style: none; color: #fff; }
  .back-contact li { font-size: 11.2px; height: 18px; display: flex; align-items: center; gap: 9px; }
  .back-contact li:first-child { font-weight: 700; }
  .back-contact svg { width: 10px; height: 10px; fill: var(--red); }

  .stamp-box { position: absolute; left: 547px; top: 72px; width: 70px; height: 84px; border: 1px solid #555; }
  .address-line { position: absolute; left: 396px; width: 240px; height: 1px; background: var(--rule); }
</style>
</head>
<body>

<section class="postcard postcard--front">
  <svg class="shapes" viewBox="0 0 659 512" width="659" height="512">
    <defs>
      <linearGradient id="photoTone" x1="0" y1="0" x2="1" y2="1">
        <stop offset="0" stop-color="var(--photo-a)"/>
        <stop offset="1" stop-color="var(--photo-b)"/>
      </linearGradient>
      <linearGradient id="redBand" x1="0" y1="0" x2="1" y2="0">
        <stop offset="0" stop-color="var(--red-deep)"/>
        <stop offset="0.5" stop-color="var(--red)"/>
        <stop offset="1" stop-color="var(--red-deep)"/>
      </linearGradient>
    </defs>
    <path fill="url(#redBand)"
      d="M0 205 C60 225 120 215 160 190 C240 260 340 325 440 335 C520 340 600 320 659 265 L659 400 C480 405 250 425 0 440 Z"/>
    <path role="img" aria-label="Photo of two women choosing a floral dress in a clothing boutique"
      fill="url(#photoTone)"
      d="M317 0 L659 0 L659 265 C600 320 520 340 440 335 C340 325 240 260 160 190 C200 120 250 50 317 0 Z"/>
    <path fill="var(--charcoal)" d="M282 0 L317 0 C250 50 200 120 160 190 L150 186 C185 110 232 45 282 0 Z"/>
    <path fill="none" stroke="#fff" stroke-width="5" d="M160 190 C240 260 340 325 440 335 C520 340 600 320 659 265"/>
    <path fill="none" stroke="#fff" stroke-width="4" d="M0 205 C60 225 120 215 158 192"/>
    <path fill="#fff" d="M0 440 C250 425 480 405 659 400 L659 406 C470 410 260 434 0 452 Z"/>
    <path fill="var(--red)" d="M0 452 C260 434 470 410 659 406 L659 410 C470 416 260 446 0 464 Z"/>
    <path fill="var(--charcoal)" d="M0 464 C260 446 470 416 659 410 L659 512 L0 512 Z"/>
  </svg>

  <div class="brand"><span class="brand__dot"></span>MAPLE ROW</div>

  <div class="offer offer__now">Now</div>
  <div class="offer offer__program">Maple Row Rewards</div>
  <div class="offer offer__more">Offers you even more</div>
  <div class="offer__amount">$15</div>
  <div class="offer__label">Reward Gift Card</div>

  <ul class="front-contact">
    <li>555-014-0124 <svg viewBox="0 0 12 12"><path d="M2 1l2.5 0 1 3-1.5 1a7 7 0 0 0 3 3l1-1.5 3 1V11C5 11 1 7 1 2z"/></svg></li>
    <li>hello@maplerowshop.com <svg viewBox="0 0 12 12"><path d="M1 3h10v7H1z"/></svg></li>
    <li>www.maplerowshop.com <svg viewBox="0 0 12 12"><circle cx="6" cy="6" r="5"/></svg></li>
  </ul>
</section>

<section class="postcard postcard--back">
  <svg class="shapes" viewBox="0 0 659 510" width="659" height="510">
    <path fill="var(--red)" d="M0 0 L530 0 C470 25 425 50 398 80 L0 80 Z"/>
    <path fill="var(--charcoal)" d="M0 335 L322 335 C316 380 302 408 282 422 L0 422 Z"/>
    <path fill="var(--ink)" d="M520 0 C420 50 350 110 335 230 C325 330 310 400 272 422 L290 422 C325 400 340 330 350 235 C365 115 440 45 560 0 Z"/>
    <path fill="none" stroke="var(--red)" stroke-width="3" d="M575 0 C460 55 375 125 362 240 C352 340 335 400 296 424"/>
  </svg>

  <h1 class="thanks">Thank You for Shopping</h1>

  <div class="letter">
    <div class="letter__wrap"></div>
    <p class="letter__greeting">Dear Customer Rewards members,</p>
    <p class="letter__body">Thank you for being such a great partner with us here at Maple Row . We hope that you are enjoying being a part of this exclusive program and know that we appreciate your business. Don't forget about your Maple Row perks-- super fast, FREE shipping and treats galore! Included in your mailer are a few exciting press hits. Also included is the New Style Studio Training Kit. Please reach out to your Maple Row Sales Reps to get more details on our new products.</p>
    <p class="letter__sign">Maple Row</p>
  </div>

  <ul class="back-contact">
    <li><svg viewBox="0 0 12 12"><path d="M2 1l2.5 0 1 3-1.5 1a7 7 0 0 0 3 3l1-1.5 3 1V11C5 11 1 7 1 2z"/></svg>555-014-0124</li>
    <li><svg viewBox="0 0 12 12"><path d="M6 0a4 4 0 0 1 4 4c0 3-4 8-4 8S2 7 2 4a4 4 0 0 1 4-4z"/></svg>48 Birch Lane, Fairview, IL 60000</li>
    <li><svg viewBox="0 0 12 12"><path d="M1 3h10v7H1z"/></svg>hello@maplerowshop.com</li>
    <li><svg viewBox="0 0 12 12"><circle cx="6" cy="6" r="5"/></svg>www.maplerowshop.com</li>
  </ul>

  <div class="stamp-box"></div>
  <div class="address-line" style="top:272px"></div>
  <div class="address-line" style="top:305px"></div>
  <div class="address-line" style="top:340px"></div>
</section>

</body>
</html>
```